Bright Fern Custom Homes business card. Double sided. Modern. professional

Bright Fern Custom Homes
contemporary modern design with our logo /
Double sided with all our contact information
Use same Green colors as in our Logo. Contemporary logo that grabs your attention. Visually pleasing and balanced. Easy to read, and Vibrant. Would love an option for rounded edges. Embossed logo would be amazing.
Contact Information for Business Card
Dana Welk Owner / General Contractor Bright Fern Custom Homes p: 704.552.1830 m: 912.648.2071 e: brightferncustomhomes@mailbox.example w: www.brightferncustomhomes.example 218 Pryor Meadow Lane Larkwood, GA 29041

```html
<!DOCTYPE html>
<html lang="en">
<head>
<meta charset="utf-8">
<title>Bright Fern Custom Homes – Business Card</title>
<link href="https://fonts.googleapis.com/css2?family=Cinzel:wght@500&family=Open+Sans:wght@400;600&display=swap" rel="stylesheet">
<style>
  :root {
    --backdrop: #1a1a1a;
    --green-dark: #5b6f31;
    --green-light: #6f8d36;
    --green-ink: #5b7227;
    --card-pale: #edebec;
    --white: #ffffff;
  }
  * { margin: 0; padding: 0; box-sizing: border-box; }
  html, body { width: 1075px; height: 1200px; overflow: hidden; background: var(--backdrop); }
  .canvas { position: relative; width: 1075px; height: 1200px; }
  .card {
    position: absolute; width: 663px; height: 395px; overflow: hidden;
    box-shadow: 3px 3px 4px rgba(0,0,0,0.6);
  }
  .card--front {
    left: 206px; top: 187px;
    background: linear-gradient(90deg, var(--green-dark) 0%, var(--green-dark) 55%, var(--green-light) 100%);
    color: var(--white);
    font-family: "Open Sans", sans-serif;
  }
  .card--back { left: 203px; top: 637px; background: var(--card-pale); }
  .brand-art {
    position: absolute; right: 0; top: 0; width: 290px; height: 395px;
    background: radial-gradient(ellipse at 55% 45%, rgba(255,255,255,0.18) 0%, rgba(255,255,255,0.06) 55%, rgba(255,255,255,0) 80%);
  }
  .person { position: absolute; left: 35px; top: 58px; }
  .person__name { font-family: "Cinzel", serif; font-weight: 500; font-size: 26px; line-height: 28px; letter-spacing: 0.5px; }
  .person__role { font-size: 16px; line-height: 20px; }
  .address { position: absolute; left: 35px; top: 158px; font-size: 17px; line-height: 23.5px; font-style: normal; }
  .address__company { font-weight: 600; }
  .contact { position: absolute; left: 35px; top: 266px; list-style: none; font-size: 17px; line-height: 23.5px; }
  .contact li { display: flex; align-items: center; gap: 6px; }
  .contact svg { width: 17px; height: 17px; flex: none; }
  .wordmark {
    position: absolute; left: 0; right: 0; top: 270px; text-align: center;
    font-family: "Cinzel", serif; font-weight: 500; font-size: 30px;
    letter-spacing: 2px; color: var(--green-ink);
  }
  .wordmark__dot {
    position: absolute; left: 50%; top: 100px; width: 54px; height: 54px;
    margin-left: -27px; border-radius: 50%; background: var(--green-ink);
  }
</style>
</head>
<body>
<main class="canvas">
  <section class="card card--front">
    <div class="brand-art" role="img" aria-label="Company symbol area in light green"></div>
    <div class="person">
      <h1 class="person__name">DANA WELK</h1>
      <p class="person__role">Owner / General Contractor</p>
    </div>
    <address class="address">
      <div class="address__company">Bright Fern Custom Homes</div>
      <div>218 Pryor Meadow Lane</div>
      <div>Larkwood, GA 29041</div>
    </address>
    <ul class="contact">
      <li><svg viewBox="0 0 24 24" fill="none" stroke="#fff" stroke-width="2.2"><path d="M5 3h4l2 5-2.5 1.5a11 11 0 0 0 6 6L16 13l5 2v4a2 2 0 0 1-2 2A16 16 0 0 1 3 5a2 2 0 0 1 2-2z"/></svg>704.552.1830</li>
      <li><svg viewBox="0 0 24 24" fill="none" stroke="#fff" stroke-width="2.2"><rect x="6" y="2" width="12" height="20" rx="2"/><line x1="10" y1="18" x2="14" y2="18"/></svg>912.648.2071</li>
      <li><svg viewBox="0 0 24 24" fill="#fff"><path d="M2 5h20v14H2z"/><path d="M2 5l10 8 10-8" fill="none" stroke="#5b6f31" stroke-width="2"/></svg>brightferncustomhomes@mailbox.example</li>
      <li><svg viewBox="0 0 24 24" fill="none" stroke="#fff" stroke-width="2"><circle cx="12" cy="12" r="10"/><ellipse cx="12" cy="12" rx="4" ry="10"/><line x1="2" y1="12" x2="22" y2="12"/></svg>www.brightferncustomhomes.example</li>
    </ul>
  </section>

  <section class="card card--back">
    <div class="wordmark__dot"></div>
    <div class="wordmark">BRIGHT FERN CUSTOM HOMES</div>
  </section>
</main>
</body>
</html>
```